Plakat-Design für eine Budgetplanung für ein Kinderbuch
Das vorgeschlagene Poster war von Anfang an unser Favorit. Es zeichnet sich aus, durch ein ansprechendes, klares und kindgerechtes Design. Wir haben die ausgesprochen zuverlässige Arbeit und Kommunikation sehr geschätzt und hoffen auf weitere Zusammenarbeit.
Zielgruppe
Wir sind ein Verlag und bringen nächsten Monat zwei Kinder-/Jugendbücher mit dem Thema Finanzbildung heraus. Das Alter der Zielgruppe ist zwischen 8 und 13 Jahren. Zu den Büchern gehört ein hochwertiges Posterset aus drei Postern. In diesem Auftrag soll zunächst das erste Poster designed werden. Hier geht es darum eine kleine 'Budgetplanung' zu erstellen. In weiteren Aufträgen sollen auch Illustrationen aufgewertet und Designs für Websites erstellt werden.
Aufgabenstellung
Wir werden einige Bilder bereitstellen, die verarbeitet werden dürfen (es müssen nicht alle verwendet werden!). Es wäre schön, wenn das Posterdesign so ausgelegt wird, dass die Bilder gut in das Gesamtdesign passen. Die Bildqualität des Posters soll auf DINA2 optimiert sein. Weiterhin stellen wir einen 'Beispiel-Geldplan' zur Verfügung, der alle Texte enthält, die das Poster beinhalten soll. Das Design dieses Beispiel-Geldplans soll unberücksichtigt bleiben. Das Gesamtdesign soll hochwertig und kreativ sein.

```html
<!DOCTYPE html>
<html lang="de">
<head>
<meta charset="utf-8">
<title>Wie ich mir meine Träume erfülle</title>
<link rel="stylesheet" href="https://fonts.googleapis.com/css2?family=Itim&family=Libre+Franklin:wght@400&display=swap">
<style>
  :root {
    --sun: #fbd93b;
    --ground: #fcc22a;
    --ink: #3b4a8c;
    --field: rgba(255, 244, 180, 0.55);
    --field-line: #f5c63a;
    --orange: #f58a4a;
    --blue: #2f9be0;
    --gold: #fff04a;
  }
  * { margin: 0; padding: 0; box-sizing: border-box; }
  html, body { width: 848px; height: 1200px; overflow: hidden; background: var(--sun); }
  .poster { position: relative; width: 848px; height: 1200px; background: var(--sun); overflow: hidden; color: var(--ink); }
  .ground { position: absolute; left: 0; top: 0; }
  .title {
    position: absolute; left: 0; top: 46px; width: 858px; text-align: center;
    font-family: "Itim", cursive; font-size: 52px; line-height: 63px; font-weight: 400;
    text-shadow: 1px 2px 2px rgba(120, 90, 0, 0.35);
    -webkit-text-stroke: 1px var(--ink);
  }
  .label, .sub, .note, .closing {
    position: absolute; white-space: nowrap;
  }
  .label { font-family: "Itim", cursive; font-size: 30px; line-height: 1; }
  .label.right, .sub.right { transform: translateX(-100%); }
  .sub { font-family: "Libre Franklin", sans-serif; font-size: 19px; line-height: 1; }
  .note { font-family: "Itim", cursive; font-size: 19px; line-height: 1; transform: translateX(-50%); }
  .saved { position: absolute; left: 375px; top: 828px; width: 216px; text-align: center; font-family: "Itim", cursive; font-size: 30px; line-height: 34px; }
  .closing { left: 40px; top: 1030px; width: 400px; text-align: center; font-family: "Itim", cursive; font-size: 38px; line-height: 52px; }
  .field { position: absolute; width: 136px; background: var(--field); border-radius: 12px; }
  .field.single { height: 34px; }
  .field.triple { height: 103px; }
  .field.triple::before, .field.triple::after {
    content: ""; position: absolute; left: 2px; right: 2px; height: 1px; background: var(--field-line);
  }
  .field.triple::before { top: 35px; }
  .field.triple::after { top: 68px; }
  .art { position: absolute; border-radius: 40px; }
  .art.money-creature { left: 561px; top: 111px; width: 237px; height: 363px; background: radial-gradient(ellipse at 60% 55%, var(--orange) 0%, rgba(245,138,74,0.5) 55%, rgba(251,217,59,0) 75%); }
  .art.rainbow { left: 0; top: 537px; width: 200px; height: 350px; border-radius: 0 200px 0 0; background: linear-gradient(135deg, #e9453a 0%, #f7a83a 25%, #fff35a 45%, #7fd7e8 65%, #3a8fe0 82%, #a76cb0 100%); opacity: 0.55; }
  .art.gold-pile { left: 75px; top: 872px; width: 310px; height: 78px; border-radius: 60% 60% 20px 20px; background: var(--gold); }
  .art.rainbow-creature { left: 51px; top: 555px; width: 120px; height: 192px; background: radial-gradient(ellipse at 50% 55%, var(--blue) 0%, rgba(47,155,224,0.55) 55%, rgba(251,217,59,0) 75%); }
</style>
</head>
<body>
<main class="poster">
  <svg class="ground" width="848" height="1200" viewBox="0 0 848 1200" aria-hidden="true">
    <path d="M0 924 C150 905 300 925 420 950 C560 980 700 960 848 1024 L848 1200 L0 1200 Z" fill="var(--ground)"/>
  </svg>

  <h1 class="title">Wie ich mir meine<br>Träume erfülle</h1>

  <div class="art money-creature" role="img" aria-label="Orange Comicfigur hält ein großes Euro-Zeichen"></div>
  <div class="art rainbow" role="img" aria-label="Regenbogen, der in einem Goldschatz endet"></div>
  <div class="art gold-pile" role="img" aria-label="Haufen aus Goldmünzen am Ende des Regenbogens"></div>
  <div class="art rainbow-creature" role="img" aria-label="Blaue Comicfigur rutscht den Regenbogen hinunter"></div>

  <span class="label right" style="left:371px; top:238px;">Ich erhalte jeden Monat:</span>
  <div class="field single" style="left:402px; top:235px;"></div>

  <span class="sub right" style="left:365px; top:299px;">Davon Taschengeld:</span>
  <span class="sub right" style="left:370px; top:332px;">Aus meinem Verdienst:</span>
  <span class="sub right" style="left:370px; top:365px;">Durch meine Investition:</span>
  <div class="field triple" style="left:400px; top:289px;"></div>

  <span class="label right" style="left:371px; top:419px;">Ich brauche jeden Monat:</span>
  <span class="note" style="left:212px; top:458px;">(für Freizeit, Essen etc.)</span>
  <div class="field single" style="left:402px; top:414px;"></div>

  <span class="label right" style="left:592px; top:513px;">Ich möchte sparen:</span>
  <div class="field single" style="left:639px; top:507px;"></div>

  <span class="sub right" style="left:592px; top:575px;">Für Wunsch 1:</span>
  <span class="sub right" style="left:592px; top:604px;">Für Wunsch 2:</span>
  <span class="sub right" style="left:592px; top:632px;">Für Wunsch 3:</span>
  <div class="field triple" style="left:637px; top:562px;"></div>

  <span class="label right" style="left:590px; top:692px;">Ich möchte spenden:</span>
  <div class="field single" style="left:637px; top:688px;"></div>

  <span class="label right" style="left:590px; top:746px;">Ich möchte investieren:</span>
  <div class="field single" style="left:637px; top:742px;"></div>

  <p class="saved">Wieviel ich schon<br>gespart habe:</p>
  <div class="field single" style="left:637px; top:848px;"></div>

  <p class="closing">Meine Träume gehen<br>in Erfüllung in:</p>
  <span class="sub right" style="left:591px; top:1042px;">Für Wunsch 1:</span>
  <span class="sub right" style="left:591px; top:1074px;">Für Wunsch 2:</span>
  <span class="sub right" style="left:591px; top:1105px;">Für Wunsch 3:</span>
  <div class="field triple" style="left:635px; top:1025px;"></div>
</main>
</body>
</html>
```